Stationery Design Project - New innovative law firm

I need a simple design, yet the tone of the stationery set need to express modern, professionalism, smart and forward-thinking. I don’t need a business card, but require the stationery set to have:
• Design letterhead
• Design facsimile
• Design memo
The triangular logo with Halvard Lane words etc, need to be present in the stationery. The red triangular logo should not be re-designed, but feel free to play around with the placement and colours of the Halvard Lane words etc....?

Target Market(s)

Business clients

Industry/Entity Type

Business

Requirements
Must have
• The triangular logo with Halvard Lane words etc...for branding.

```html
<!DOCTYPE html>
<html lang="en">
<head>
<meta charset="utf-8">
<title>Halvard Lane — Letterhead</title>
<link href="https://fonts.googleapis.com/css2?family=Open+Sans:wght@400;700&family=Arimo:wght@400;700&display=swap" rel="stylesheet">
<style>
  :root {
    --paper: #ffffff;
    --ink: #231f20;
    --muted: #58595b;
    --brand-red: #d9261c;
  }
  * { margin: 0; padding: 0; box-sizing: border-box; }
  html, body {
    width: 917px;
    height: 1200px;
    overflow: hidden;
    background: var(--paper);
  }
  .letterhead {
    position: relative;
    width: 917px;
    height: 1200px;
    background: var(--paper);
    color: var(--ink);
  }
  .brand {
    position: absolute;
    top: 38px;
    left: 566px;
    display: flex;
    flex-direction: column;
    align-items: flex-start;
  }
  .brand-row {
    display: flex;
    align-items: center;
    gap: 10px;
  }
  .brand-square {
    width: 22px;
    height: 22px;
    background: var(--brand-red);
  }
  .brand-name {
    font-family: "Open Sans", sans-serif;
    font-weight: 700;
    font-size: 29px;
    line-height: 1;
    letter-spacing: 2px;
    text-transform: uppercase;
    color: var(--ink);
  }
  .brand-tagline {
    margin-top: 7px;
    margin-left: 31px;
    font-family: "Open Sans", sans-serif;
    font-weight: 400;
    font-size: 13px;
    letter-spacing: 0.3px;
    text-transform: uppercase;
    color: var(--muted);
  }
  .contact {
    position: absolute;
    left: 593px;
    top: 1103px;
    font-family: "Arimo", sans-serif;
    font-size: 12.5px;
    line-height: 14.7px;
    color: var(--ink);
    list-style: none;
  }
  .contact-label { font-weight: 700; }
</style>
</head>
<body>
  <main class="letterhead">
    <header class="brand">
      <div class="brand-row">
        <span class="brand-square" aria-hidden="true"></span>
        <span class="brand-name">Halvard Lane</span>
      </div>
      <span class="brand-tagline">Accounting, Tax, Business Advice &amp; Legal</span>
    </header>

    <ul class="contact">
      <li><span class="contact-label">Address:</span> 27 Wattle Grove, Kedron Park, QLD 4031</li>
      <li><span class="contact-label">Mobile:</span> +61 400 172 645</li>
      <li><span class="contact-label">E-mail:</span> j.morrow@halvardlane.com.au</li>
      <li><span class="contact-label">Web:</span> www.halvardlane.com.au</li>
    </ul>
  </main>
</body>
</html>
```